Dawn Harbor Goods Vitamin C Serum

We need a product label and box designed for our Vitamin C Serum product. The label will go on a 2oz bottle and the box will hold the 2oz bottle. Attached are the box and label templates as well as a Vitamin C Serum we have with another brand.

For this brand, we're looking to have the product look high end/luxury.

Target Market(s)

40+ year old women

```html
<!DOCTYPE html>
<html lang="en">
<head>
<meta charset="utf-8">
<title>Dawn Harbor Goods – Vitamin C Facial Serum Packaging</title>
<link rel="stylesheet" href="https://fonts.googleapis.com/css2?family=Barlow+Semi+Condensed:wght@400;500;600&display=swap">
<style>
  :root {
    --bg: #efecf4;
    --panel: #f8f8f7;
    --orange: #ea7725;
    --orange-deep: #e1601b;
    --orange-soft: #f4a34c;
    --orange-pale: #f9c99a;
    --yellow: #f6c92a;
    --green: #8cc43f;
    --green-deep: #5f9a2c;
    --ink: #2f2f2f;
    --pattern: #ececec;
  }
  * { margin: 0; padding: 0; box-sizing: border-box; }
  html, body { width: 1200px; height: 789px; overflow: hidden; }
  body {
    background: var(--bg);
    font-family: "Barlow Semi Condensed", "Arial Narrow", sans-serif;
    color: var(--ink);
    position: relative;
  }
  .panel {
    position: absolute;
    background: var(--panel);
    overflow: hidden;
    box-shadow: 0 2px 10px rgba(60, 40, 90, 0.12);
  }
  .panel svg { position: absolute; inset: 0; }
  .box-front { left: 330px; top: 25px; width: 200px; height: 740px; }
  .bottle-label { left: 640px; top: 100px; width: 420px; height: 590px; }

  .brand-name {
    position: absolute; left: 0; right: 0;
    display: flex; align-items: center; justify-content: center; gap: 6px;
    font-weight: 600; color: var(--orange); letter-spacing: 0.02em;
  }
  .brand-dot { border-radius: 50%; background: var(--orange); flex: none; }

  .vitamin-tag {
    position: absolute; background: #fff; color: var(--orange);
    font-weight: 500; line-height: 1; padding: 2px 6px 1px 14px;
    transform-origin: left center;
  }
  .product-type {
    position: absolute; left: 0; right: 0; text-align: center;
    font-weight: 500; letter-spacing: 0.02em; color: var(--ink);
  }
  .product-type::after {
    content: ""; display: block; margin: 3px auto 0;
    height: 1px; background: #8a8a8a;
  }
  .ingredient-box {
    position: absolute; border: 1.5px solid var(--green);
    color: var(--green); text-align: center; font-weight: 500;
    line-height: 1.0; background: rgba(255,255,255,0.6);
  }
  .tagline {
    position: absolute; left: 0; right: 0; text-align: center;
    color: var(--orange); font-weight: 500;
  }
  .volume {
    position: absolute; left: 0; right: 0; text-align: center;
    color: var(--ink); font-weight: 400;
  }

  /* box front type */
  .box-front .brand-name { top: 160px; font-size: 15px; }
  .box-front .brand-dot { width: 9px; height: 9px; }
  .box-front .vitamin-tag { left: 82px; top: 292px; font-size: 23px; transform: rotate(-8deg); }
  .box-front .product-type { top: 430px; font-size: 15px; transform: rotate(-8deg); }
  .box-front .product-type::after { width: 50px; }
  .box-front .ingredient-box { left: 34px; top: 568px; width: 132px; padding: 3px 0; font-size: 13px; transform: rotate(-8deg); }
  .box-front .tagline { top: 624px; font-size: 14px; transform: rotate(-8deg); }
  .box-front .volume { top: 698px; font-size: 11px; transform: rotate(-8deg); }

  /* bottle label type */
  .bottle-label .brand-name { top: 100px; font-size: 20px; }
  .bottle-label .brand-dot { width: 11px; height: 11px; }
  .bottle-label .vitamin-tag { left: 214px; top: 218px; font-size: 30px; transform: rotate(-3deg); }
  .bottle-label .product-type { top: 338px; font-size: 21px; }
  .bottle-label .product-type::after { width: 70px; }
  .bottle-label .ingredient-box { left: 163px; top: 456px; width: 110px; padding: 3px 0; font-size: 12px; }
  .bottle-label .tagline { top: 500px; font-size: 14px; }
  .bottle-label .volume { top: 556px; font-size: 12px; }
</style>
</head>
<body>

<section class="panel box-front" aria-label="Box front panel">
  <svg width="200" height="740" viewBox="0 0 200 740">
    <defs>
      <linearGradient id="boxPatternFill" x1="0" y1="0" x2="0" y2="1">
        <stop offset="0" stop-color="#f6f6f6"/>
        <stop offset="1" stop-color="var(--pattern)"/>
      </linearGradient>
      <linearGradient id="boxSwoosh" x1="0" y1="0" x2="1" y2="0">
        <stop offset="0" stop-color="#e8671e"/>
        <stop offset="1" stop-color="#f7b27a"/>
      </linearGradient>
      <radialGradient id="boxOrangeSlice" cx="0.5" cy="0.5" r="0.5">
        <stop offset="0" stop-color="#fbd08a"/>
        <stop offset="1" stop-color="#f39a2e"/>
      </radialGradient>
      <linearGradient id="boxAloe" x1="0" y1="0" x2="0" y2="1">
        <stop offset="0" stop-color="#a6d65c"/>
        <stop offset="1" stop-color="#4f8f2a"/>
      </linearGradient>
    </defs>
    <rect class="panel-ground" width="200" height="740" fill="var(--panel)"/>
    <rect role="img" aria-label="Subtle concentric circle background pattern" x="0" y="380" width="200" height="360" fill="url(#boxPatternFill)"/>
    <rect class="top-band" x="0" y="8" width="200" height="64" fill="var(--orange)"/>
    <polygon class="swoosh-glow" points="0,330 200,262 200,380 0,448" fill="var(--orange-pale)" opacity="0.7"/>
    <polygon class="swoosh-main" points="0,340 200,272 200,328 0,408" fill="url(#boxSwoosh)"/>
    <polygon class="swoosh-stripe" points="0,372 200,300 200,312 0,388" fill="var(--orange-deep)"/>
    <circle role="img" aria-label="Orange slice illustration" cx="72" cy="318" r="56" fill="url(#boxOrangeSlice)" stroke="#fff" stroke-width="3"/>
    <rect role="img" aria-label="Aloe vera plant illustration" x="52" y="472" width="96" height="90" rx="10" fill="url(#boxAloe)"/>
    <path role="img" aria-label="Yellow lotus petals" d="M0,740 L0,688 Q100,630 200,680 L200,740 Z" fill="var(--yellow)"/>
  </svg>
  <div class="brand-name"><span class="brand-dot"></span>Dawn Harbor Goods</div>
  <div class="vitamin-tag">VITAMIN</div>
  <div class="product-type">FACIAL SERUM</div>
  <div class="ingredient-box">VITAMIN E &amp;<br>ALOEVERA</div>
  <div class="tagline">Brighter &amp; Healthier Skin</div>
  <div class="volume">2 oz/60ml</div>
</section>

<section class="panel bottle-label" aria-label="Bottle label">
  <svg width="420" height="590" viewBox="0 0 420 590">
    <defs>
      <linearGradient id="labelPatternFill" x1="0" y1="0" x2="0" y2="1">
        <stop offset="0" stop-color="#f6f6f6"/>
        <stop offset="1" stop-color="var(--pattern)"/>
      </linearGradient>
      <linearGradient id="labelSwoosh" x1="0" y1="0" x2="1" y2="0">
        <stop offset="0" stop-color="#e4611c"/>
        <stop offset="1" stop-color="#f4a14e"/>
      </linearGradient>
      <radialGradient id="labelOrangeSlice" cx="0.5" cy="0.5" r="0.5">
        <stop offset="0" stop-color="#fbd08a"/>
        <stop offset="1" stop-color="#f39a2e"/>
      </radialGradient>
      <linearGradient id="labelAloe" x1="0" y1="0" x2="0" y2="1">
        <stop offset="0" stop-color="#a6d65c"/>
        <stop offset="1" stop-color="#4f8f2a"/>
      </linearGradient>
    </defs>
    <rect class="panel-ground" width="420" height="590" fill="var(--panel)"/>
    <rect role="img" aria-label="Subtle concentric circle background pattern" x="0" y="320" width="420" height="270" fill="url(#labelPatternFill)"/>
    <rect class="top-band" x="0" y="0" width="420" height="44" fill="var(--orange)"/>
    <polygon class="swoosh-glow" points="28,190 395,150 395,290 28,320" fill="var(--orange-pale)" opacity="0.75"/>
    <polygon class="swoosh-main" points="28,200 395,168 395,276 28,300" fill="url(#labelSwoosh)"/>
    <polygon class="swoosh-stripe" points="28,236 395,214 395,226 28,250" fill="var(--orange-deep)"/>
    <circle role="img" aria-label="Orange slice illustration" cx="180" cy="238" r="70" fill="url(#labelOrangeSlice)" stroke="#fff" stroke-width="4"/>
    <rect role="img" aria-label="Aloe vera plant illustration" x="172" y="378" width="92" height="70" rx="10" fill="url(#labelAloe)"/>
    <path role="img" aria-label="Yellow lotus petals" d="M150,590 L150,560 Q218,520 286,560 L286,590 Z" fill="var(--yellow)"/>
  </svg>
  <div class="brand-name"><span class="brand-dot"></span>Dawn Harbor Goods</div>
  <div class="vitamin-tag">VITAMIN</div>
  <div class="product-type">FACIAL SERUM</div>
  <div class="ingredient-box">VITAMIN E &amp;<br>ALOEVERA</div>
  <div class="tagline">Brighter &amp; Healthier Skin</div>
  <div class="volume">2 oz/60ml</div>
</section>

</body>
</html>
```